Business Card Design Project

Mabel's Tonics is a natural skincare business and we need a business card designed. The company focuses on natural products and will be launching with body scrubs and bath fizzies and our mission statement is: To deliver high quality natural beauty products at a good value. It's two cards - one design - the only information changing would be name and email address

Target Market(s)

Females ages 20-50

Industry/Entity Type

Business

Requirements
Must have
• Mabel's Tonics

Corinne Halvorsen-Pitt
T: 800-417-9368
E: Corinne@MabelsTonics.example
W: www.MabelsTonics.example

Ulrich Benedetti
T: 800-417-9368
E: Ulrich@MabelsTonics.example
W: www.MabelsTonics.example
Nice to have
• I'd like to use the colors or text found at www.mabelstonics.example but I'm open to suggestions since design isn't set in stone yet. I would also like to have the words .....a little bit of magic somewhere under the company name in a different type of font. I would like a design that feels clean and maybe a retro feel to it - front and back would be nice but not mandatory

```html
<!DOCTYPE html>
<html lang="en">
<head>
<meta charset="utf-8">
<title>Mabel's Tonics – Business Cards</title>
<link rel="stylesheet" href="https://fonts.googleapis.com/css2?family=Questrial&family=Quicksand:wght@500&display=swap">
<style>
  :root {
    --page-bg: #ffffff;
    --card-purple: #7b1f86;
    --card-purple-deep: #621772;
    --card-edge: #b48fd0;
    --art-gold: #f2b638;
    --art-orange: #f08a24;
    --art-violet: #8c3fae;
    --art-cloud: #cdb8e6;
    --text-light: #ffffff;
    --logo-pink: #f6a8d8;
    --grommet-light: #eeeeee;
    --grommet-dark: #8c8c8c;
  }
  * { box-sizing: border-box; margin: 0; padding: 0; }
  html, body {
    width: 1200px;
    height: 900px;
    overflow: hidden;
    background: var(--page-bg);
  }
  .canvas {
    position: relative;
    width: 1200px;
    height: 900px;
    font-family: "Questrial", sans-serif;
    color: var(--text-light);
  }
  .card {
    position: absolute;
    border-radius: 18px;
    overflow: hidden;
    background: var(--card-purple);
    box-shadow: inset 0 0 0 5px var(--card-edge), 0 2px 4px rgba(0,0,0,0.18);
  }
  .card--front { left: 34px; top: 4px; width: 704px; height: 424px; }
  .card--back-landscape { left: 30px; top: 452px; width: 708px; height: 424px; }
  .card--back-portrait { left: 754px; top: 173px; width: 428px; height: 704px; }

  .front-art {
    position: absolute;
    inset: 0;
    background:
      radial-gradient(ellipse 60% 40% at 30% 105%, var(--art-cloud) 0%, rgba(205,184,230,0) 70%),
      radial-gradient(ellipse 45% 35% at 85% 100%, var(--art-cloud) 0%, rgba(205,184,230,0) 70%),
      linear-gradient(120deg, var(--art-orange) 0%, var(--art-gold) 22%, var(--art-violet) 45%, var(--card-purple) 75%, var(--card-purple-deep) 100%);
  }
  .back-art {
    position: absolute;
    inset: 0;
    background:
      radial-gradient(ellipse 55% 50% at 80% 20%, rgba(240,140,150,0.35) 0%, rgba(240,140,150,0) 70%),
      radial-gradient(ellipse 60% 40% at 90% 100%, rgba(230,215,245,0.55) 0%, rgba(230,215,245,0) 70%),
      linear-gradient(160deg, var(--card-purple) 0%, var(--card-purple-deep) 100%);
  }
  .card--back-portrait .back-art {
    background:
      radial-gradient(ellipse 60% 45% at 35% 15%, rgba(240,140,150,0.35) 0%, rgba(240,140,150,0) 70%),
      radial-gradient(ellipse 50% 60% at 100% 85%, rgba(230,215,245,0.55) 0%, rgba(230,215,245,0) 70%),
      linear-gradient(160deg, var(--card-purple) 0%, var(--card-purple-deep) 100%);
  }

  .grommet {
    position: absolute;
    width: 40px;
    height: 40px;
    border-radius: 50%;
    background: radial-gradient(circle, var(--page-bg) 0 42%, var(--grommet-light) 46% 70%, var(--grommet-dark) 100%);
    transform: translate(-50%, -50%);
  }

  .tagline {
    position: absolute;
    right: 44px;
    top: 120px;
    font-family: "Quicksand", sans-serif;
    font-weight: 500;
    font-size: 22px;
    color: var(--text-light);
  }
  .brand-name {
    position: absolute;
    right: 38px;
    top: 148px;
    font-family: "Questrial", sans-serif;
    font-size: 44px;
    color: var(--logo-pink);
    white-space: nowrap;
  }

  .person-name {
    position: absolute;
    font-size: 40px;
    white-space: nowrap;
  }
  .card--back-landscape .person-name { left: 0; right: 0; top: 150px; text-align: center; }

  .contact {
    position: absolute;
    list-style: none;
    font-size: 23px;
    line-height: 31px;
  }
  .card--back-landscape .contact { left: 46px; top: 290px; }

  .vertical {
    position: absolute;
    writing-mode: vertical-rl;
    transform: rotate(180deg);
    white-space: nowrap;
  }
  .card--back-portrait .person-name { left: 150px; top: 0; height: 704px; display: flex; align-items: center; justify-content: center; font-size: 40px; }
  .card--back-portrait .contact { left: 296px; bottom: 40px; top: auto; line-height: 33px; }
</style>
</head>
<body>
<div class="canvas">

  <section class="card card--front">
    <div class="front-art" role="img" aria-label="Illustration of golden paper planes flying through purple swirls, stars and soft lavender clouds"></div>
    <span class="grommet" style="left:602px; top:32px;"></span>
    <p class="tagline">a little bit of magic</p>
    <p class="brand-name">Mabel's Tonics</p>
  </section>

  <section class="card card--back-landscape">
    <div class="back-art" role="img" aria-label="Faint paper planes, swirls and clouds on a purple background"></div>
    <span class="grommet" style="left:46px; top:34px;"></span>
    <h2 class="person-name">Corinne Halvorsen-Pitt</h2>
    <ul class="contact">
      <li>T: 800-417-9368</li>
      <li>E: Corinne@MabelsTonics.example</li>
      <li>W: www.MabelsTonics.example</li>
    </ul>
  </section>

  <section class="card card--back-portrait">
    <div class="back-art" role="img" aria-label="Faint paper planes, swirls and clouds on a purple background"></div>
    <span class="grommet" style="left:46px; top:647px;"></span>
    <h2 class="person-name"><span class="vertical" style="position:static;">Ulrich Benedetti</span></h2>
    <ul class="contact vertical">
      <li>T: 800-417-9368</li>
      <li>E: Ulrich@MabelsTonics.example</li>
      <li>W: www.mabelstonics.example</li>
    </ul>
  </section>

</div>
</body>
</html>
```